Stunning website design for world's unique software

Design only (No coding required)
This website design is linked with a logo design and illustration design contests.

Industry/Entity Type

Software

```html
<!DOCTYPE html>
<html lang="en">
<head>
<meta charset="utf-8">
<title>Kestrel — Unique Experiences for Web & Mobile</title>
<link href="https://fonts.googleapis.com/css2?family=Oswald:wght@300;400&family=Arimo:wght@400&display=swap" rel="stylesheet">
<style>
:root{
  --orange:#ee6a0c;
  --ink:#2b2b2b;
  --body:#6b6b6b;
  --header-bg:#f2f2f2;
  --band:#efefef;
  --footer:#2f2f2f;
  --footer-line:#444;
  --white:#fff;
}
*{margin:0;padding:0;box-sizing:border-box}
html,body{width:922px;height:1200px;overflow:hidden;background:var(--white)}
body{position:relative;font-family:"Arimo",Arial,sans-serif;color:var(--body)}

/* header */
.site-header{position:absolute;left:0;top:0;width:922px;height:75px;background:var(--header-bg)}
.brand{position:absolute;left:88px;top:18px;display:flex;align-items:center;gap:8px}
.brand-dot{width:38px;height:38px;border-radius:50%;background:var(--orange)}
.brand-name{font-family:"Oswald",sans-serif;font-size:28px;font-weight:400;color:var(--ink);letter-spacing:.5px}
.main-nav a{position:absolute;top:0;height:75px;line-height:72px;font-family:"Oswald",sans-serif;font-size:15px;color:#666;text-decoration:none;transform:translateX(-50%)}
.main-nav a.active{background:var(--orange);color:var(--white);width:63px;text-align:center}

/* hero */
.hero{position:absolute;left:0;top:75px;width:922px;height:240px;background:linear-gradient(110deg,#bdbdbd 0%,#f4f4f4 22%,#cfcfcf 45%,#e9e9e9 70%,#b5b5b5 100%)}
.hero h1{position:absolute;left:90px;top:65px;font-family:"Oswald",sans-serif;font-weight:300;font-size:32px;line-height:40px;color:var(--orange);letter-spacing:-.5px;transform:scaleX(.85);transform-origin:left top;white-space:nowrap}
.hero-devices{position:absolute;left:506px;top:15px;width:323px;height:220px;border-radius:12px;background:linear-gradient(160deg,#3a3a3a 0%,#d9d9d9 40%,#eaeaea 70%,#9a9a9a 100%)}

/* features */
.feature{position:absolute;top:325px;width:186px}
.feature-icon{position:absolute;width:56px;height:56px;border-radius:50%;background:var(--orange);top:0}
.feature-icon svg{position:absolute;left:14px;top:14px}
.feature h3{position:absolute;top:57px;width:260px;text-align:center;font-family:"Oswald",sans-serif;font-weight:400;font-size:20px;color:var(--ink)}
.feature p{position:absolute;top:99px;left:0;width:184px;font-size:10px;line-height:17.6px}
.feature p span{display:block;white-space:nowrap;text-align:justify;text-align-last:justify}

/* options */
.options{position:absolute;left:0;top:510px;width:922px;height:240px;background:var(--band)}
.options-shot{position:absolute;left:64px;top:8px;width:348px;height:226px;background:linear-gradient(180deg,#e4e4e4,#f7f7f7);border:1px solid #d6d6d6}
.round-badge{position:absolute;width:40px;height:40px;border-radius:50%;background:var(--orange)}
.round-badge svg{position:absolute;left:10px;top:10px}
.options h2{position:absolute;left:512px;top:14px;font-family:"Oswald",sans-serif;font-weight:400;font-size:18px;color:var(--ink)}
.accent{color:var(--orange)}
.options p{position:absolute;left:470px;width:382px;font-size:10.4px;line-height:17.6px}
.ticks{position:absolute;left:468px;top:108px;width:400px;display:grid;grid-template-columns:200px 200px;row-gap:2.5px;font-size:10.4px;line-height:17px;list-style:none}
.ticks li{display:flex;align-items:center;gap:6px}
.learn-more{position:absolute;right:77px;top:206px;font-family:"Oswald",sans-serif;font-size:15px;color:var(--orange);text-decoration:underline}

/* testimonials */
.testi-head{position:absolute;left:404px;top:763px;font-family:"Oswald",sans-serif;font-weight:400;font-size:19px;color:var(--ink)}
.testimonial{position:absolute;width:380px;height:64px}
.portrait{position:absolute;left:0;top:0;width:66px;height:64px;background:linear-gradient(160deg,#e6e6e6,#c9b9a5)}
.qmark{position:absolute;font-family:Georgia,serif;font-size:40px;line-height:40px;color:#9a9a9a;font-weight:bold}
.testimonial p{position:absolute;left:94px;top:2px;width:268px;font-size:10.4px;line-height:13.6px}
.testimonial .who{position:absolute;left:276px;top:52px;font-size:11px;color:var(--orange)}

/* footer */
.site-footer{position:absolute;left:0;top:988px;width:922px;height:212px;background:var(--footer)}
.site-footer h4{position:absolute;top:10px;font-family:"Oswald",sans-serif;font-weight:400;font-size:15px;color:var(--orange)}
.footer-nav{position:absolute;left:77px;top:34px;list-style:none;font-family:"Oswald",sans-serif;font-size:15px;line-height:24px;color:var(--white)}
.post{position:absolute;left:265px;width:200px;height:34px}
.post-thumb{position:absolute;left:0;top:0;width:47px;height:34px;background:linear-gradient(180deg,#cfcfcf,#f1f1f1)}
.post-title{position:absolute;left:51px;top:1px;font-size:10.4px;color:var(--white);white-space:nowrap}
.post-meta{position:absolute;left:51px;top:15px;font-size:9px;color:#ddd}
.contact-list{position:absolute;left:471px;top:36px;list-style:none;font-size:11px;line-height:20.8px;color:#e8e8e8}
.social{position:absolute;width:36px;height:36px;border-radius:50%;border:2px solid var(--orange);background:#3a3a3a}
.footer-rule{position:absolute;left:0;top:174px;width:922px;height:1px;background:var(--footer-line)}
.copyright{position:absolute;left:0;top:188px;width:922px;text-align:center;font-size:9.6px;color:#ddd}
</style>
</head>
<body>

<header class="site-header">
  <div class="brand"><span class="brand-dot"></span><span class="brand-name">kestrel</span></div>
  <nav class="main-nav">
    <a class="active" href="#" style="left:430px">Home</a>
    <a href="#" style="left:508px">Features</a>
    <a href="#" style="left:591px">Work</a>
    <a href="#" style="left:666px">Pricing</a>
    <a href="#" style="left:741px">Shop</a>
    <a href="#" style="left:820px">Contact</a>
  </nav>
</header>

<section class="hero">
  <h1>UNIQUE EXPERIENCES FOR<br>WEB &amp; MOBILE</h1>
  <div class="hero-devices" role="img" aria-label="Smartphone and desktop monitor showing the wireless device pairing and client devices layout screens"></div>
</section>

<section class="features">
  <div class="feature" style="left:68px">
    <div class="feature-icon" style="left:56px"><svg width="28" height="28" viewBox="0 0 28 28"><path d="M5 23C5 12 12 5 24 5c0 12-7 18-17 18" fill="#fff"/><path d="M5 24L16 13" stroke="var(--orange)" stroke-width="2"/></svg></div>
    <h3 style="left:-34px">Expressive Design</h3>
    <p><span>Lorem Ipsum is simply dummy text</span><span>of the printing and typesetting</span><span>industry. Lorem Ipsum has been the</span><span>industry's standard dummy text ever.</span></p>
  </div>
  <div class="feature" style="left:270px">
    <div class="feature-icon" style="left:52px"><svg width="28" height="28" viewBox="0 0 28 28"><path d="M7 22a5 5 0 010-10 7 7 0 0113-1 5 5 0 011 11z" fill="#fff"/></svg></div>
    <h3 style="left:-50px">Easy Configuration</h3>
    <p><span>Lorem Ipsum is simply dummy text</span><span>of the printing and typesetting</span><span>industry. Lorem Ipsum has been the</span><span>industry's standard dummy text ever.</span></p>
  </div>
  <div class="feature" style="left:470px">
    <div class="feature-icon" style="left:52px"><svg width="28" height="28" viewBox="0 0 28 28" fill="none" stroke="#fff" stroke-width="2.6" stroke-linecap="round"><path d="M3 11a16 16 0 0122 0"/><path d="M7 15a10 10 0 0114 0"/><path d="M11 19a4 4 0 016 0"/><circle cx="14" cy="23" r="1.6" fill="#fff" stroke="none"/></svg></div>
    <h3 style="left:-50px">Huge Analytics</h3>
    <p><span>Lorem Ipsum is simply dummy text</span><span>of the printing and typesetting</span><span>industry. Lorem Ipsum has been the</span><span>industry's standard dummy text ever.</span></p>
  </div>
  <div class="feature" style="left:672px">
    <div class="feature-icon" style="left:58px"><svg width="28" height="28" viewBox="0 0 28 28" fill="#fff"><rect x="2" y="20" width="3" height="4"/><rect x="7" y="17" width="3" height="7"/><rect x="12" y="13" width="3" height="11"/><rect x="17" y="9" width="3" height="15"/><rect x="22" y="4" width="3" height="20"/></svg></div>
    <h3 style="left:-44px">Tuned to Perfection</h3>
    <p><span>Lorem Ipsum is simply dummy text</span><span>of the printing and typesetting</span><span>industry. Lorem Ipsum has been the</span><span>industry's standard dummy text ever.</span></p>
  </div>
</section>

<section class="options">
  <div class="options-shot" role="img" aria-label="Software window showing device pairing, client devices layout and device properties"></div>
  <div class="round-badge" style="left:468px;top:6px"><svg width="20" height="20" viewBox="0 0 20 20" fill="#fff"><path d="M10 2L1 10h3v8h5v-5h2v5h5v-8h3z"/></svg></div>
  <h2><span class="accent">KESTREL</span> Very powerful options built right in</h2>
  <p style="top:46px">Lorem Ipsum is simply dummy text of the printing and typesetting industry. Lorem Ipsum has been the industry's standard dummy text ever since the 1500s, when an unknown printer took a galley of type and scrambled it to make a type.</p>
  <ul class="ticks">
    <li><svg width="14" height="12" viewBox="0 0 14 12"><path d="M1 6l4 4 8-9" fill="none" stroke="#aaa" stroke-width="2.4"/></svg>Lorem Ipsum is simply dummy text</li>
    <li><svg width="14" height="12" viewBox="0 0 14 12"><path d="M1 6l4 4 8-9" fill="none" stroke="#aaa" stroke-width="2.4"/></svg>Lorem Ipsum is simply dummy text</li>
    <li><svg width="14" height="12" viewBox="0 0 14 12"><path d="M1 6l4 4 8-9" fill="none" stroke="#aaa" stroke-width="2.4"/></svg>Lorem Ipsum is simply dummy text</li>
    <li><svg width="14" height="12" viewBox="0 0 14 12"><path d="M1 6l4 4 8-9" fill="none" stroke="#aaa" stroke-width="2.4"/></svg>Lorem Ipsum is simply dummy text</li>
    <li><svg width="14" height="12" viewBox="0 0 14 12"><path d="M1 6l4 4 8-9" fill="none" stroke="#aaa" stroke-width="2.4"/></svg>Lorem Ipsum is simply dummy text</li>
    <li><svg width="14" height="12" viewBox="0 0 14 12"><path d="M1 6l4 4 8-9" fill="none" stroke="#aaa" stroke-width="2.4"/></svg>Lorem Ipsum is simply dummy text</li>
  </ul>
  <p style="top:168px">Lorem Ipsum is simply dummy text of the printing and typesetting industry. Lorem Ipsum has been the industry's standard dummy text ever since the 1500s.</p>
  <a class="learn-more" href="#">Learn More</a>
</section>

<section class="testimonials">
  <div class="round-badge" style="left:356px;top:756px"><svg width="20" height="20" viewBox="0 0 20 20" fill="#fff"><rect x="1" y="8" width="4" height="10"/><path d="M6 8l4-7c2 0 2 2 1.5 5H18l-2 12H6z"/></svg></div>
  <h2 class="testi-head"><span class="accent">Client</span> Testimonial</h2>

  <div class="testimonial" style="left:81px;top:805px">
    <div class="portrait" role="img" aria-label="Portrait photo of client"></div>
    <span class="qmark" style="left:70px;top:-2px">&ldquo;</span>
    <p>Lorem Ipsum is simply dummy text of the printing and typesetting industry. Lorem Ipsum has ben the industry's standard dummy text ever since the 1500s, when an unknown printer took.</p>
    <span class="who">- Client Name</span>
    <span class="qmark" style="left:346px;top:44px">&rdquo;</span>
  </div>
  <div class="testimonial" style="left:475px;top:805px">
    <div class="portrait" role="img" aria-label="Portrait photo of client"></div>
    <span class="qmark" style="left:70px;top:-2px">&ldquo;</span>
    <p>Lorem Ipsum is simply dummy text of the printing and typesetting industry. Lorem Ipsum has ben the industry's standard dummy text ever since the 1500s, when an unknown printer took.</p>
    <span class="who">- Client Name</span>
    <span class="qmark" style="left:346px;top:44px">&rdquo;</span>
  </div>
  <div class="testimonial" style="left:81px;top:893px">
    <div class="portrait" role="img" aria-label="Portrait photo of client"></div>
    <span class="qmark" style="left:70px;top:-2px">&ldquo;</span>
    <p>Lorem Ipsum is simply dummy text of the printing and typesetting industry. Lorem Ipsum has ben the industry's standard dummy text ever since the 1500s, when an unknown printer took.</p>
    <span class="who">- Client Name</span>
    <span class="qmark" style="left:346px;top:44px">&rdquo;</span>
  </div>
  <div class="testimonial" style="left:475px;top:893px">
    <div class="portrait" role="img" aria-label="Portrait photo of client"></div>
    <span class="qmark" style="left:70px;top:-2px">&ldquo;</span>
    <p>Lorem Ipsum is simply dummy text of the printing and typesetting industry. Lorem Ipsum has ben the industry's standard dummy text ever since the 1500s, when an unknown printer took.</p>
    <span class="who">- Client Name</span>
    <span class="qmark" style="left:346px;top:44px">&rdquo;</span>
  </div>
</section>

<footer class="site-footer">
  <ul class="footer-nav">
    <li class="accent" style="position:absolute;top:-26px">Home</li>
    <li>Features</li><li>Work</li><li>Pricing</li><li>Shop</li><li>Contact</li>
  </ul>

  <h4 style="left:265px">From the Blog</h4>
  <div class="post" style="top:36px"><div class="post-thumb" role="img" aria-label="Blog post thumbnail"></div><span class="post-title">Lorem Ipsum is simply dummy</span><span class="post-meta">19 Oct 2012 | <span class="accent">By Admin</span></span></div>
  <div class="post" style="top:79px"><div class="post-thumb" role="img" aria-label="Blog post thumbnail"></div><span class="post-title">Lorem Ipsum is simply dummy</span><span class="post-meta">19 Oct 2012 | <span class="accent">By Admin</span></span></div>
  <div class="post" style="top:122px"><div class="post-thumb" role="img" aria-label="Blog post thumbnail"></div><span class="post-title">Lorem Ipsum is simply dummy</span><span class="post-meta">19 Oct 2012 | <span class="accent">By Admin</span></span></div>

  <h4 style="left:474px">Get In Touch</h4>
  <ul class="contact-list">
    <li>Office No., Building name,</li>
    <li>Area name,</li>
    <li>City, State, Country</li>
    <li>Call : +44 100 200 3000</li>
    <li>Fax : +44 100 200 3000</li>
    <li>Email : info@kestrelsoft.com</li>
  </ul>

  <h4 style="left:682px">Get In Touch</h4>
  <span class="social" style="left:686px;top:39px"></span>
  <span class="social" style="left:740px;top:39px"></span>
  <span class="social" style="left:793px;top:39px"></span>
  <span class="social" style="left:686px;top:92px"></span>
  <span class="social" style="left:740px;top:92px"></span>
  <span class="social" style="left:793px;top:92px"></span>

  <div class="footer-rule"></div>
  <p class="copyright">© <span class="accent">KESTREL</span> - 2014. All Rights Reserved.</p>
</footer>

</body>
</html>
```